Visitenkarte erstellen für Reiki Praxis

Visitenkarten für Reiki Praxis Doppelseitig

business cards reiki practice double-sided

The background can also be a different color

```html
<!DOCTYPE html>
<html lang="en">
<head>
<meta charset="UTF-8">
<title>Radiant Flow – Business Card, Both Sides</title>
<link href="https://fonts.googleapis.com/css2?family=Open+Sans:wght@400;600&family=Arimo:wght@400;700&display=swap" rel="stylesheet">
<style>
  :root {
    --stage: #3a3a3c;
    --card-black: #1b1b1b;
    --card-white: #ffffff;
    --gold: #e9b12f;
    --text-white: #ffffff;
    --text-dark: #2a2a2a;
  }
  html, body {
    margin: 0;
    padding: 0;
    width: 1200px;
    height: 896px;
    overflow: hidden;
    background: var(--stage);
  }
  .canvas {
    position: relative;
    width: 1200px;
    height: 896px;
  }
  .card {
    position: absolute;
    top: 133px;
    width: 360px;
    height: 630px;
    border-radius: 26px;
    overflow: hidden;
    box-shadow: 0 12px 30px rgba(0,0,0,0.45);
  }
  .card--back {
    left: 180px;
    background: var(--card-black);
  }
  .card--front {
    left: 660px;
    background: var(--card-white);
  }
  .brand {
    position: absolute;
    left: 0;
    right: 0;
    text-align: center;
  }
  .card--back .brand { top: 270px; }
  .card--front .brand { top: 60px; }
  .brand__name {
    font-family: "Open Sans", sans-serif;
    font-weight: 400;
    font-size: 27px;
    letter-spacing: 0.5px;
    color: var(--text-white);
    display: inline-flex;
    align-items: center;
    gap: 10px;
  }
  .brand__mark {
    width: 12px;
    height: 12px;
    border-radius: 50%;
    background: var(--text-white);
    display: inline-block;
  }
  .brand__owner {
    margin-top: 2px;
    font-family: "Open Sans", sans-serif;
    font-size: 16px;
    letter-spacing: 5px;
    color: var(--gold);
  }
  .front__top {
    position: absolute;
    top: 0;
    left: 0;
  }
  .person {
    position: absolute;
    top: 360px;
    left: 0;
    right: 0;
    text-align: center;
  }
  .person__name {
    font-family: "Arimo", sans-serif;
    font-weight: 700;
    font-size: 30px;
    letter-spacing: 1px;
    color: var(--gold);
  }
  .person__role {
    font-family: "Arimo", sans-serif;
    font-size: 12px;
    letter-spacing: 1px;
    color: var(--text-dark);
    margin-top: 2px;
  }
  .divider {
    position: absolute;
    top: 425px;
    left: 36px;
    width: 288px;
    height: 22px;
  }
  .contact {
    position: absolute;
    top: 462px;
    left: 0;
    right: 0;
    text-align: center;
    font-family: "Arimo", sans-serif;
    font-size: 17px;
    line-height: 26px;
    color: var(--text-dark);
  }
</style>
</head>
<body>
<main class="canvas">

  <section class="card card--back" aria-label="Card back">
    <div class="brand">
      <div class="brand__name"><span class="brand__mark"></span>RADIANT FLOW</div>
      <div class="brand__owner">MARA LINDT</div>
    </div>
  </section>

  <section class="card card--front" aria-label="Card front">
    <svg class="front__top" width="360" height="630" viewBox="0 0 360 630">
      <path d="M0 0 H360 V330 C330 322 300 318 270 300 C240 282 210 300 180 296 C140 290 120 250 90 236 C60 222 30 232 0 240 Z" fill="var(--card-black)"/>
    </svg>
    <div class="brand">
      <div class="brand__name"><span class="brand__mark"></span>RADIANT FLOW</div>
      <div class="brand__owner">MARA LINDT</div>
    </div>

    <div class="person">
      <div class="person__name">DANIEL BROOKS</div>
      <div class="person__role">DIRECTOR</div>
    </div>

    <svg class="divider" viewBox="0 0 288 22" aria-hidden="true">
      <g stroke="var(--gold)" fill="none" stroke-width="1.4">
        <line x1="0" y1="11" x2="100" y2="11"/>
        <line x1="188" y1="11" x2="288" y2="11"/>
        <circle cx="116" cy="11" r="8"/>
        <circle cx="144" cy="11" r="8"/>
        <circle cx="172" cy="11" r="8"/>
        <path d="M113 7 q0 8 7 8 l1 -2 -2 -1 -1 1 q-2 -1 -3 -3 l1 -1 -1 -2 z" stroke-width="1"/>
        <rect x="139" y="8" width="10" height="7" stroke-width="1"/>
        <path d="M139 8 l5 4 l5 -4" stroke-width="1"/>
        <circle cx="172" cy="11" r="4.5" stroke-width="1"/>
        <line x1="167.5" y1="11" x2="176.5" y2="11" stroke-width="1"/>
        <ellipse cx="172" cy="11" rx="2" ry="4.5" stroke-width="1"/>
      </g>
    </svg>

    <div class="contact">
      <div>330 555 0142</div>
      <div>info@radiantflow.com</div>
      <div>www.radiantflow.com</div>
    </div>
  </section>

</main>
</body>
</html>
```